Health & Nutrition - Business Cards

Needs to look new-age, simple, and elegant. The cards are for my services/counsel in health and nutrition - which include mind, body, and soul. I would like to see something clean and simple but beautiful. Can have a plain background or with a pattern but I don't want it to take away from my contact details. Therefore, my info can be on the back of the card and a nice front design. I really like the flower of life symbol. The name of my business is called Willow Lantern.

Target Market(s)

Clients - men & women age 20-60. Adults, parents, teachers, sick individuals seeking nutrient counseling and dietary management.

Industry/Entity Type

Nutritionist

Contact Information for Business Card

Tomas Brindle
Cell: 345-582-7046
Email: tbrindle@mailvane.net

Colors
33a6d7
33b8a4
add136
ffffff
5c5c5c
f04a50
fbee3f
cedeed
85cae6

Requirements
Nice to have
• Maybe it can have some sort of sacred geometry as well, but not required. Nice to have the colors that I choose in the project but feel free to come up with your own use of colors. Thanks! =)

```html
<!DOCTYPE html>
<html lang="en">
<head>
<meta charset="utf-8">
<title>Willow Lantern – Business Cards</title>
<link rel="stylesheet" href="https://fonts.googleapis.com/css2?family=Montserrat:wght@400;500&display=swap">
<style>
  :root {
    --stage: #474747;
    --card-front: #ffffff;
    --card-back: #f2f2f4;
    --frame-peach: #fbe0cc;
    --brand-red: #ea1c24;
    --brand-green: #a3cb38;
    --ink-brown: #5a3b2a;
    --tile-peach: #fde1c8;
    --tile-cream: #fdf0d6;
    --tile-blue: #d3d9e3;
    --tile-mint: #dcece8;
    --tile-taupe: #d9c9c0;
  }
  * { margin: 0; padding: 0; box-sizing: border-box; }
  html, body { width: 1200px; height: 1000px; overflow: hidden; }
  body {
    background: var(--stage);
    font-family: "Montserrat", sans-serif;
    position: relative;
  }
  .card {
    position: absolute;
    left: 230px;
    width: 753px;
    height: 420px;
    box-shadow: 3px 4px 6px rgba(0,0,0,0.35);
    overflow: hidden;
  }
  .card--front { top: 51px; background: var(--card-front); }
  .card--back  { top: 500px; background: var(--card-back); }

  .pattern-tile { position: absolute; }
  .tile-peach { background: linear-gradient(135deg, var(--tile-peach), var(--tile-cream)); }
  .tile-blue  { background: linear-gradient(135deg, var(--tile-blue), var(--tile-mint)); }
  .tile-mixed { background: linear-gradient(135deg, var(--tile-peach), var(--tile-blue)); }
  .tile-taupe { background: linear-gradient(135deg, var(--tile-taupe), var(--tile-peach)); }
  .tile-cream { background: var(--tile-cream); }
  .tile-mint  { background: linear-gradient(135deg, var(--tile-mint), var(--tile-blue)); }

  .brand-panel {
    position: absolute;
    left: 162px; top: 99px;
    width: 430px; height: 222px;
    background: var(--card-front);
    border: 4px solid var(--frame-peach);
    display: flex;
    flex-direction: column;
    align-items: center;
    justify-content: center;
    text-align: center;
  }
  .brand-name {
    font-weight: 500;
    font-size: 45px;
    line-height: 50px;
    letter-spacing: 1px;
    text-transform: uppercase;
  }
  .brand-name__first { color: var(--brand-red); }
  .brand-name__second { color: var(--brand-green); }

  .contact {
    position: absolute;
    left: 0; right: 0; top: 155px;
    text-align: center;
    color: var(--ink-brown);
    font-weight: 400;
    font-size: 30px;
    line-height: 39px;
    letter-spacing: 4px;
    text-transform: uppercase;
  }
</style>
</head>
<body>
  <section class="card card--front">
    <div class="pattern-tile tile-mixed" style="left:0;top:0;width:76px;height:251px" role="img" aria-label="Pastel triangle pattern"></div>
    <div class="pattern-tile tile-blue" style="left:84px;top:0;width:183px;height:92px" role="img" aria-label="Pastel triangle pattern"></div>
    <div class="pattern-tile tile-peach" style="left:275px;top:0;width:122px;height:92px" role="img" aria-label="Polka dot pattern"></div>
    <div class="pattern-tile tile-cream" style="left:405px;top:0;width:133px;height:92px" role="img" aria-label="Cream stripe pattern"></div>
    <div class="pattern-tile tile-blue" style="left:546px;top:0;width:46px;height:92px" role="img" aria-label="Blue triangle pattern"></div>
    <div class="pattern-tile tile-peach" style="left:600px;top:0;width:96px;height:129px" role="img" aria-label="Peach leaf pattern"></div>
    <div class="pattern-tile tile-mint" style="left:704px;top:0;width:49px;height:321px" role="img" aria-label="Diamond pattern"></div>
    <div class="pattern-tile tile-mint" style="left:84px;top:99px;width:70px;height:152px" role="img" aria-label="Mint stripe pattern"></div>
    <div class="pattern-tile tile-taupe" style="left:600px;top:136px;width:96px;height:103px" role="img" aria-label="Polka dot pattern"></div>
    <div class="pattern-tile tile-blue" style="left:600px;top:246px;width:96px;height:75px" role="img" aria-label="Blue stripe pattern"></div>
    <div class="pattern-tile tile-mixed" style="left:0;top:259px;width:154px;height:161px" role="img" aria-label="Leaf pattern"></div>
    <div class="pattern-tile tile-blue" style="left:162px;top:329px;width:358px;height:91px" role="img" aria-label="Diamond pattern"></div>
    <div class="pattern-tile tile-peach" style="left:528px;top:329px;width:225px;height:91px" role="img" aria-label="Peach triangle pattern"></div>

    <div class="brand-panel">
      <h1 class="brand-name">
        <span class="brand-name__first">Willow</span><br>
        <span class="brand-name__second">Lantern</span>
      </h1>
    </div>
  </section>

  <section class="card card--back">
    <div class="contact">
      <p class="contact__name">Tomas Brindle</p>
      <p class="contact__phone">345-582-7046</p>
      <p class="contact__email">tbrindle@mailvane.net</p>
    </div>
  </section>
</body>
</html>
```